Brindlewood Property Management, L.L.C
Brindlewood Property Management, L.L.C - Financial Services
Creative Brief
Professional
Doreen Whitlock,CAM
President
P.O. Box 572816 Naples, FL. 34117
info@brindlewoodprop.com
www.brindlewoodprop.com
I am open to clear business cards or two sides if a two sided design is used see comment below.
Logo on back of card if this option is designed

```html
<!DOCTYPE html>
<html lang="en">
<head>
<meta charset="utf-8">
<title>Brindlewood Property Management – Stationery</title>
<link href="https://fonts.googleapis.com/css2?family=Open+Sans:wght@400;600;700&display=swap" rel="stylesheet">
<style>
:root{
  --bg:#f1f1f2;
  --paper:#ffffff;
  --navy:#16215e;
  --blue:#1f3fa3;
  --bright:#2f8fe0;
  --sky:#6fc3f2;
  --ink:#333a48;
  --line:#6b6f78;
  --dark:#141926;
}
*{box-sizing:border-box;margin:0;padding:0}
html,body{width:1200px;height:695px;overflow:hidden;background:var(--bg);font-family:"Open Sans",Arial,sans-serif;color:var(--ink)}
.canvas{position:relative;width:1200px;height:695px;background:linear-gradient(#f7f7f8,#e9e9eb)}
.sheet{position:absolute;background:var(--paper);box-shadow:0 1px 4px rgba(0,0,0,.22);overflow:hidden}
.letter{top:233px;width:352px;height:434px}
.fax{left:24px}
.letterhead{left:398px}
.brand{position:absolute;display:flex;flex-direction:column;align-items:center;gap:3px}
.brand-dot{width:20px;height:20px;border-radius:50%;background:var(--blue)}
.brand-name{font-weight:700;color:var(--navy);font-size:8px;letter-spacing:.6px}
.letter .brand{left:12px;top:12px}
.contact{position:absolute;font-size:4.2px;line-height:6px;color:var(--line)}
.letter .contact{right:24px;top:14px}
.fax-title{position:absolute;right:24px;top:60px;font-size:15px;color:#222}
.fax-table{position:absolute;left:12px;top:80px;width:322px;border-collapse:collapse;font-size:5px}
.fax-table td{border:1px solid #444;height:16px;padding:0 3px;vertical-align:middle}
.fax-table .label{width:40px}
.checks{position:absolute;left:12px;top:177px;display:flex;gap:18px;font-size:5px}
.checks span{display:flex;align-items:center;gap:3px}
.checks span::before{content:"";width:7px;height:7px;border:1px solid #444}
.faint-mark{position:absolute;right:18px;bottom:28px;width:92px;height:92px;border-radius:50%;background:radial-gradient(circle at 35% 30%,#fff,#e7e9ee)}
.sheet-band{position:absolute;left:0;right:0;bottom:26px;height:12px;background:linear-gradient(90deg,var(--navy),var(--blue) 40%,var(--bright) 75%,var(--sky))}
.footer-url{position:absolute;right:24px;bottom:10px;font-size:4.5px;color:var(--line)}
.card{position:absolute;width:128px;height:104px;box-shadow:0 1px 3px rgba(0,0,0,.3);overflow:hidden}
.card svg{position:absolute;inset:0}
.card .brand{left:0;right:0;top:28px}
.card-front{background:radial-gradient(circle at 50% 35%,var(--bright),var(--blue) 55%,var(--navy))}
.card-front .brand-name,.env-back .brand-name{color:#fff}
.card-front .brand-dot,.env-back .brand-dot{background:#fff}
.card-back{background:#fff}
.card-dark{background:linear-gradient(135deg,#2a3242,var(--dark))}
.card-text{position:absolute;font-size:4.4px;line-height:6px;color:var(--ink)}
.card-text b{display:block;font-size:5.5px;color:var(--navy)}
.envelope{position:absolute;left:773px;width:405px}
.env-front{top:307px;height:185px}
.env-front .brand{left:14px;top:14px}
.env-front .contact{left:14px;bottom:16px}
.env-front .faint-mark{right:14px;bottom:18px;width:70px;height:70px}
.env-back{top:509px;height:170px}
.env-back svg{position:absolute;inset:0}
.env-back .brand{left:0;right:0;top:58px}
</style>
</head>
<body>
<div class="canvas">

  <section class="sheet letter fax">
    <div class="brand"><span class="brand-dot"></span><span class="brand-name">BRINDLEWOOD</span></div>
    <div class="contact">P.O. Box 1208<br>Cedar Haven, FL. 30417<br>info@brindlewoodprop.com<br>www.brindlewoodprop.com</div>
    <div class="fax-title">FAX</div>
    <table class="fax-table">
      <tr><td class="label">To:</td><td></td><td class="label">From:</td><td></td></tr>
      <tr><td class="label">Fax:</td><td></td><td class="label">Pages:</td><td></td></tr>
      <tr><td class="label">Phone:</td><td></td><td class="label">Date:</td><td></td></tr>
      <tr><td class="label">Re:</td><td></td><td class="label">CC:</td><td></td></tr>
    </table>
    <div class="checks"><span>Urgent</span><span>For Review</span><span>Please Comment</span><span>Please Reply</span><span>Please Recycle</span></div>
    <div class="faint-mark"></div>
    <div class="sheet-band"></div>
    <div class="footer-url">www.brindlewoodprop.com</div>
  </section>

  <section class="sheet letter letterhead">
    <div class="brand"><span class="brand-dot"></span><span class="brand-name">BRINDLEWOOD</span></div>
    <div class="contact">P.O. Box 1208<br>Cedar Haven, FL. 30417<br>info@brindlewoodprop.com<br>www.brindlewoodprop.com</div>
    <div class="faint-mark"></div>
    <div class="sheet-band"></div>
    <div class="footer-url">www.brindlewoodprop.com</div>
  </section>

  <div class="card card-front" style="left:468px;top:29px">
    <div class="brand"><span class="brand-dot"></span><span class="brand-name">BRINDLEWOOD</span></div>
  </div>
  <div class="card card-back" style="left:604px;top:29px;width:186px">
    <svg viewBox="0 0 186 104" preserveAspectRatio="none"><polygon points="150,0 186,0 186,104 110,104" fill="#1f3fa3"/><polygon points="140,0 150,0 110,104 100,104" fill="#6fc3f2"/></svg>
    <div class="card-text" style="left:12px;top:14px"><b>Doreen Whitlock</b>President</div>
    <div class="card-text" style="left:12px;top:60px">P.O. Box 1208<br>Cedar Haven, FL. 30417<br>info@brindlewoodprop.com</div>
  </div>

  <div class="card card-front" style="left:814px;top:29px">
    <svg viewBox="0 0 128 104"><polygon points="60,104 128,30 128,104" fill="#16215e" opacity=".55"/></svg>
    <div class="brand"><span class="brand-dot"></span><span class="brand-name">BRINDLEWOOD</span></div>
  </div>
  <div class="card card-back" style="left:942px;top:29px">
    <svg viewBox="0 0 128 104"><polygon points="0,0 70,0 0,60" fill="#1f3fa3"/><polygon points="70,0 78,0 0,68 0,60" fill="#6fc3f2"/></svg>
    <div class="card-text" style="left:56px;top:50px"><b>Doreen Whitlock</b>President<br>P.O. Box 1208<br>Cedar Haven, FL.<br>info@brindlewoodprop.com</div>
  </div>

  <div class="card card-front" style="left:814px;top:145px">
    <svg viewBox="0 0 128 104"><polygon points="0,104 70,0 90,0 20,104" fill="#6fc3f2" opacity=".35"/></svg>
    <div class="brand"><span class="brand-dot"></span><span class="brand-name">BRINDLEWOOD</span></div>
  </div>
  <div class="card card-dark" style="left:942px;top:145px">
    <svg viewBox="0 0 128 104"><polygon points="50,104 110,0 128,0 128,10 72,104" fill="#2f8fe0"/></svg>
    <div class="card-text" style="left:10px;top:14px;color:#cfd6e4"><b style="color:#fff">Doreen Whitlock</b>President</div>
    <div class="card-text" style="left:10px;top:70px;color:#cfd6e4">P.O. Box 1208<br>Cedar Haven, FL.</div>
  </div>

  <section class="sheet envelope env-front">
    <div class="brand"><span class="brand-dot"></span><span class="brand-name">BRINDLEWOOD</span></div>
    <div class="contact">P.O. Box 1208<br>Cedar Haven, FL. 30417<br>info@brindlewoodprop.com<br>www.brindlewoodprop.com</div>
    <div class="faint-mark"></div>
  </section>

  <section class="sheet envelope env-back">
    <svg viewBox="0 0 405 170" preserveAspectRatio="none">
      <defs><linearGradient id="flap" x1="0" y1="0" x2="1" y2="0"><stop offset="0" stop-color="#16215e"/><stop offset=".5" stop-color="#1f3fa3"/><stop offset="1" stop-color="#16215e"/></linearGradient></defs>
      <polygon points="0,0 405,0 405,62 202,122 0,62" fill="url(#flap)"/>
      <polyline points="0,62 202,122 405,62" fill="none" stroke="#6fc3f2" stroke-width="2"/>
    </svg>
    <div class="brand"><span class="brand-dot"></span><span class="brand-name">BRINDLEWOOD</span></div>
  </section>

</div>
</body>
</html>
```